Upgrades and adjustments to my existing website

I currently have a website in the trial period with NestHarbor but their template isn't meeting my site needs. My website is https://www.BrevoPlaque.example. I need the calendar to be changed. Each customer that orders a real estate sign installation from us needs to be able to request a day (not time specific) and be able to enter the address of the home where they need the sign installed. In addition, I would like a testimonials section on the website. I need someone to build the website and point it to my domain name as I do not know how to do any of that. My customers are trying to order now so every day they can't place the order I am losing money so quick turn time is important

Target Market(s)

Real Estate Agents ordering sign post installations

Industry/Entity Type

Real Estate

Coding

Coded - Design and coding required

Number of Pages Required

1 page

Font styles to use
Sans Serif

Colors
0355a3
3377b5
85abd2
0493ce
33a6d7
85cae6

Requirements
Must have
• The ability to book installation requests online with address for installation. Please see live current website I have
Nice to have
• Links to social media, ability to pay invoice on website,
Testimonial section.
Ability to track progress of installation request for customers
Ability to share the appointment calendar with my installers

```html
<!DOCTYPE html>
<html lang="en">
<head>
<meta charset="utf-8">
<title>Brevo Plaque – Solar Lit Real Estate Signs</title>
<link rel="stylesheet" href="https://fonts.googleapis.com/css2?family=Poppins:wght@300;400;500;600&display=swap">
<style>
:root{
  --navy:#0e3045;
  --ink:#17324a;
  --grey-bg:#efefef;
  --text-grey:#6a6a6a;
  --blue-dark:#0355a3;
  --blue-mid:#3377b5;
  --blue-pale:#85abd2;
  --blue-bright:#0493ce;
  --blue-sky:#33a6d7;
  --blue-soft:#85cae6;
  --wave:#1faad6;
  --white:#ffffff;
}
*{box-sizing:border-box;margin:0;padding:0}
html,body{width:1200px;height:2545px;overflow:hidden}
body{position:relative;font-family:"Poppins",sans-serif;background:var(--grey-bg);color:var(--ink)}
.abs{position:absolute}

/* hero */
.hero{position:absolute;left:0;top:0;width:1200px;height:678px;background:var(--grey-bg);overflow:hidden}
.hero-wave{position:absolute;left:0;top:0}
.hero-photo{position:absolute;left:232px;top:0;width:420px;height:415px;
  background:radial-gradient(ellipse 62% 72% at 50% 38%,#3f78a8 0%,#5d9fcf 40%,#7cc0e2 62%,rgba(124,192,226,0) 82%)}
.welcome-panel{position:absolute;left:708px;top:0;width:186px;height:307px;background:var(--navy);
  box-shadow:0 10px 16px rgba(0,0,0,.35);text-align:center;color:var(--white)}
.welcome-panel .connect{margin-top:20px;font-size:10px;letter-spacing:1px;color:var(--blue-sky)}
.social-square{width:18px;height:18px;background:var(--blue-sky);border-radius:2px;margin:10px auto 0}
.welcome-panel .welcome{margin-top:58px;font-size:18px;font-weight:500}
.brand-name{margin-top:28px;font-size:24px;font-weight:600;line-height:1.15;color:var(--white)}

.contact{position:absolute;right:739px;text-align:right;color:var(--text-grey);font-size:20px;line-height:26px}
.contact-icon{position:absolute;left:478px}
.contact-rule{position:absolute;left:225px;top:538px;width:277px;height:1px;background:#c8c8c8}

.tagline{left:571px;top:390px;font-size:18px;font-weight:500;color:var(--ink)}
.about-title{left:571px;top:436px;font-size:18px;font-weight:400;color:var(--blue-mid)}
.about-text{left:571px;top:467px;width:380px;font-size:11.5px;line-height:18.8px;font-weight:300;color:#555}

/* services */
.services{position:absolute;left:0;top:678px;width:1200px;height:450px;background:var(--white)}
.service-photo{position:absolute;left:254px;width:159px;height:132px}
.service-photo.posts{background:linear-gradient(90deg,#6b5a4a,#e9ecef 30%,#d8dde2 60%,#bfc6cc)}
.service-photo.removal{background:linear-gradient(160deg,#a9c4dc,#d8d0bf 45%,#3e5a7a 70%,#c8322f)}
.service-title{position:absolute;left:448px;font-size:18.5px;font-weight:500;color:var(--ink)}
.service-meta{position:absolute;left:449px;font-size:11.5px;color:#444}
.schedule-btn{position:absolute;left:796px;width:178px;height:48px;background:var(--blue-bright);color:var(--white);
  font-size:18px;font-weight:500;display:flex;align-items:center;justify-content:center}

/* booking */
.booking{position:absolute;left:0;top:1128px;width:1200px;height:724px;background:var(--navy);color:var(--white)}
.promo{position:absolute;right:742px;text-align:right;color:var(--blue-soft);font-weight:600}
.promo-big{font-size:37px;line-height:40px}
.promo-mid{font-size:18px;line-height:18px}
.promo-copy{position:absolute;right:742px;top:212px;text-align:right;font-size:11px;line-height:19px;font-weight:500;color:var(--white)}
.booking-rule{position:absolute;left:503px;top:93px;width:1px;height:482px;background:var(--blue-sky)}

.testimonials{position:absolute;right:742px;top:318px;width:210px;text-align:right}
.testimonials h4{font-size:13px;font-weight:600;letter-spacing:.5px;color:var(--blue-soft);margin-bottom:12px}
.quote{font-size:10.5px;line-height:16px;font-weight:300;color:var(--white);margin-bottom:4px}
.quote-by{font-size:10px;font-weight:500;color:var(--blue-sky);margin-bottom:16px}

.calendar{font-family:Arial,Helvetica,sans-serif}
.back-link{position:absolute;top:87px;font-size:11px}
.month{position:absolute;left:543px;top:126px;width:422px;font-size:10px;text-align:center}
.month-arrow{position:absolute;top:128px}
.day-grid{position:absolute;left:543px;top:160px;width:423px;display:grid;grid-template-columns:repeat(7,60.4px);grid-auto-rows:35px;font-size:11px}
.day-grid span{display:flex;align-items:center;justify-content:center}
.day-grid .head{font-weight:700}
.day-grid .open b{display:flex;align-items:center;justify-content:center;width:24px;height:24px;border:1px solid var(--white);border-radius:50%;font-weight:400}
.day-grid .today b{background:var(--white);color:var(--navy)}

.request{position:absolute;left:562px;width:384px}
.selected-day{top:382px;text-align:center;font-size:11px}
.selected-day strong{color:var(--blue-soft)}
.request-label{font-size:11px;font-weight:700;margin-bottom:6px}
.request-input{height:28px;border:1px solid var(--blue-sky);font-size:10.5px;color:var(--blue-pale);display:flex;align-items:center;padding:0 10px}
.request-btn{top:530px;height:30px;background:var(--blue-bright);font-size:11px;font-weight:700;letter-spacing:.5px;display:flex;align-items:center;justify-content:center}
.progress{position:absolute;top:667px;height:8px;width:44px}

/* contact form */
.field{position:absolute;background:var(--white);box-shadow:0 1px 3px rgba(0,0,0,.25);font-size:11px;color:#9a9a9a;padding:16px 16px}
.notice{position:absolute;left:0;top:2200px;width:1200px;text-align:center;font-size:11.5px;color:#555}
.notice strong{font-weight:600;color:#333}
.send-btn{position:absolute;left:539px;top:2245px;width:134px;height:33px;background:var(--blue-bright);color:var(--white);
  font-size:12px;font-weight:500;display:flex;align-items:center;justify-content:center}

/* footer */
.footer-wave{position:absolute;left:0;top:2320px}
.copyright{position:absolute;left:0;top:2402px;width:1200px;text-align:center;font-size:11.5px;font-weight:500;color:var(--white)}
</style>
</head>
<body>

<section class="hero">
  <svg class="hero-wave" width="1200" height="260" viewBox="0 0 1200 260" aria-hidden="true">
    <path d="M0 0H1200V110C1080 112 960 118 880 140C720 190 520 238 330 220C170 205 70 150 0 80Z" fill="var(--wave)"/>
  </svg>
  <div class="hero-photo" role="img" aria-label="Owner standing beside a white sign post with a for-sale panel"></div>

  <div class="welcome-panel">
    <p class="connect">CONNECT WITH US</p>
    <div class="social-square" aria-label="Social media page"></div>
    <p class="welcome">WELCOME TO</p>
    <p class="brand-name">BREVO<br>PLAQUE</p>
  </div>

  <p class="contact" style="top:465px">555-014-2290</p>
  <svg class="contact-icon" style="top:469px" width="18" height="20" viewBox="0 0 18 20" aria-hidden="true">
    <path d="M4 2l3 4-2 2c1 3 3 5 5 6l2-2 4 3-2 3C8 18 2 11 2 4z" fill="none" stroke="#17324a" stroke-width="1.6"/>
  </svg>
  <p class="contact" style="top:500px">Orders@BrevoPlaque.example</p>
  <svg class="contact-icon" style="top:507px" width="22" height="15" viewBox="0 0 22 15" aria-hidden="true">
    <rect x="1" y="1" width="20" height="13" fill="none" stroke="#17324a" stroke-width="1.5"/>
    <path d="M1 1l10 8 10-8M1 14l7-6M21 14l-7-6" fill="none" stroke="#17324a" stroke-width="1.3"/>
  </svg>
  <div class="contact-rule"></div>
  <p class="contact" style="top:550px">Hours: Open today</p>
  <svg class="contact-icon" style="top:553px" width="24" height="24" viewBox="0 0 24 24" aria-hidden="true">
    <circle cx="12" cy="12" r="10" fill="none" stroke="#17324a" stroke-width="1.8"/>
    <path d="M12 6v6h5" fill="none" stroke="#17324a" stroke-width="1.8"/>
  </svg>
  <p class="contact" style="top:576px;right:762px">08:00 am – 05:00 pm</p>
  <svg class="abs" style="left:442px;top:587px" width="14" height="9" viewBox="0 0 14 9" aria-hidden="true">
    <path d="M0 0h14L7 9z" fill="var(--blue-soft)"/>
  </svg>

  <h1 class="abs tagline">DON’T SELL YOUR HOME IN THE DARK</h1>
  <h2 class="abs about-title">ABOUT BREVO PLAQUE</h2>
  <p class="abs about-text">We install solar powered lit real estate signs to make your home stand out and get it sold. We use treated wood posts with powder-coated steel bases for high quality, looks and durability. Your order includes storage, maintenance, and installation of your panels and riders within 48 hours, as well as free pick-up and removal. We are fully insured. Our Owner and Operator, Marek, is committed to providing an excellent product and exceptional service.</p>
</section>

<section class="services">
  <div class="service-photo posts" style="top:60px" role="img" aria-label="Row of white sign posts stored in a garage"></div>
  <h3 class="service-title" style="top:108px">REAL ESTATE SIGN INSTALLATION</h3>
  <p class="service-meta" style="top:139px">1 hr &nbsp;|&nbsp; Price varies</p>
  <div class="schedule-btn" style="top:105px">SHCEDULE</div>

  <div class="service-photo removal" style="top:250px" role="img" aria-label="Owner loading a removed sign post onto a truck"></div>
  <h3 class="service-title" style="top:302px">SIGN REMOVAL</h3>
  <p class="service-meta" style="top:333px">1 hr &nbsp;|&nbsp; FREE</p>
  <div class="schedule-btn" style="top:304px">SHCEDULE</div>
</section>

<section class="booking">
  <div class="promo" style="top:88px">
    <div class="promo-big">INSTALL</div>
    <div class="promo-mid">WITHIN</div>
    <div class="promo-big" style="margin-top:6px">48 HOURS</div>
  </div>
  <p class="promo-copy">ONLINE REQUESTS.<br>SELECT ANY DAY<br>AND WE WILL INSTALL<br>WITHIN 48 HOURS</p>

  <div class="testimonials">
    <h4>WHAT AGENTS SAY</h4>
    <p class="quote">“Signs went up the next morning and the lit panel gets noticed every evening.”</p>
    <p class="quote-by">— Carla Vennt, Listing Agent</p>
    <p class="quote">“Ordering is simple and pick-up after closing is always on time.”</p>
    <p class="quote-by">— Owen Thale, Broker</p>
  </div>

  <div class="booking-rule"></div>

  <div class="calendar">
    <svg class="abs" style="left:538px;top:90px" width="6" height="8" viewBox="0 0 6 8" aria-hidden="true"><path d="M6 0v8L0 4z" fill="#fff"/></svg>
    <p class="back-link" style="left:549px">View all services</p>
    <p class="month">March 2021</p>
    <svg class="month-arrow" style="left:566px" width="8" height="12" viewBox="0 0 8 12" aria-hidden="true"><path d="M8 0v12L0 6z" fill="#fff"/></svg>
    <svg class="month-arrow" style="left:932px" width="8" height="12" viewBox="0 0 8 12" aria-hidden="true"><path d="M0 0v12l8-6z" fill="#fff"/></svg>

    <div class="day-grid">
      <span class="head">Su</span><span class="head">Mo</span><span class="head">Tu</span><span class="head">We</span><span class="head">Th</span><span class="head">Fr</span><span class="head">Sa</span>
      <span></span><span>1</span><span>2</span><span>3</span><span>4</span><span>5</span><span>6</span>
      <span>7</span><span>8</span><span>9</span><span>10</span><span class="open today"><b>11</b></span><span class="open"><b>12</b></span><span class="open"><b>13</b></span>
      <span class="open"><b>14</b></span><span class="open"><b>15</b></span><span class="open"><b>16</b></span><span class="open"><b>17</b></span><span class="open"><b>18</b></span><span class="open"><b>19</b></span><span class="open"><b>20</b></span>
      <span class="open"><b>21</b></span><span class="open"><b>22</b></span><span class="open"><b>23</b></span><span class="open"><b>24</b></span><span class="open"><b>25</b></span><span class="open"><b>26</b></span><span class="open"><b>27</b></span>
      <span class="open"><b>28</b></span><span class="open"><b>29</b></span><span class="open"><b>30</b></span><span class="open"><b>31</b></span>
    </div>

    <p class="request selected-day">Requested day: <strong>Thursday, March 11, 2021</strong> (no set time)</p>
    <div class="request" style="top:414px">
      <p class="request-label">Installation address</p>
      <div class="request-input">Street address, city, ZIP</div>
    </div>
    <div class="request" style="top:470px">
      <p class="request-label">Notes for installer</p>
      <div class="request-input">Gate code, rider panels, placement</div>
    </div>
    <div class="request request-btn">REQUEST THIS DAY</div>
  </div>

  <div class="progress" style="left:479px;background:var(--blue-dark)"></div>
  <div class="progress" style="left:546px;background:var(--blue-mid)"></div>
  <div class="progress" style="left:611px;background:var(--blue-pale)"></div>
  <div class="progress" style="left:677px;background:var(--blue-bright)"></div>
</section>

<form class="contact-form">
  <div class="field" style="left:314px;top:1930px;width:267px;height:46px">Name</div>
  <div class="field" style="left:606px;top:1930px;width:267px;height:46px">Email</div>
  <div class="field" style="left:314px;top:2000px;width:558px;height:154px">Message</div>
  <p class="notice">This site is protected by FormGuard and the Veridian <strong>Privacy Policy</strong> and <strong>Terms of Service</strong> apply.</p>
  <div class="send-btn">Send</div>
</form>

<svg class="footer-wave" width="1200" height="225" viewBox="0 0 1200 225" aria-hidden="true">
  <path d="M0 78C300 72 640 20 920 14C1060 12 1150 45 1200 80V225H0Z" fill="#0a8fc4"/>
  <path d="M0 82C300 78 640 28 920 22C1060 20 1150 60 1200 100V225H0Z" fill="var(--wave)"/>
</svg>
<p class="copyright">Copyright © 2021 BREVO PLAQUE - All rights reserved.</p>

</body>
</html>
```